Pet business needs a business card

Pet shop needs a business card. Like dark background and and debased look.

Hedgerowpups
Lindelaan 27
B - 3270 Korbeek
Belgium

www.hedgerowpups.example
mail@hedgerowpups.example
Phone +32471869203

I will ad a tagline shortly.

Industry/Entity Type

Shop

Font styles to use
Sans Serif

Requirements
Must have
• Must be possible to print the card debased. See example image.

```html
<!DOCTYPE html>
<html lang="en">
<head>
<meta charset="utf-8">
<title>Hedgerowpups – Business Card</title>
<link rel="stylesheet" href="https://fonts.googleapis.com/css2?family=Roboto:wght@400;700;900&display=swap">
<style>
  :root {
    --stage: #262626;
    --orange: #f0a13e;
    --olive-grey: #6a695b;
    --paper: #ffffff;
    --ink: #5a594d;
  }
  * { box-sizing: border-box; margin: 0; padding: 0; }
  html, body {
    width: 1200px; height: 900px; overflow: hidden;
    background: var(--stage);
    font-family: "Roboto", Arial, sans-serif;
  }
  .stage {
    width: 1200px; height: 900px;
    display: flex; align-items: center; justify-content: center; gap: 40px;
  }
  .card {
    position: relative;
    width: 540px; height: 350px;
    overflow: hidden;
    box-shadow: 0 10px 30px rgba(0,0,0,.5);
  }
  .card__shapes { position: absolute; inset: 0; width: 100%; height: 100%; }
  .paw { position: absolute; }
  .paw--grey { fill: var(--olive-grey); }
  .paw--orange { fill: var(--orange); }

  /* Front */
  .card--front { background: var(--orange); }
  .front__name {
    position: absolute; left: 48px; top: 205px;
    font-weight: 900; font-size: 44px; letter-spacing: -0.5px;
    color: var(--ink);
  }
  .card--front .paw--grey { left: 392px; top: 4px; width: 70px; height: 60px; }
  .card--front .paw--orange { left: 438px; top: 150px; width: 86px; height: 74px; }

  /* Back */
  .card--back { background: var(--olive-grey); }
  .back__name {
    position: absolute; left: 34px; top: 14px;
    font-weight: 900; font-size: 30px; color: var(--ink);
  }
  .back__contact {
    position: absolute; right: 32px; top: 78px;
    text-align: right; color: var(--paper);
    font-style: normal; font-size: 17px; line-height: 1.35;
  }
  .back__contact .gap { display: block; height: 18px; }
  .card--back .paw--orange { left: 32px; top: 104px; width: 80px; height: 70px; }
  .card--back .paw--grey { left: 52px; top: 290px; width: 70px; height: 60px; }
</style>
</head>
<body>
<svg width="0" height="0" style="position:absolute" aria-hidden="true">
  <symbol id="paw" viewBox="0 0 100 86">
    <ellipse cx="14" cy="38" rx="11" ry="13"/>
    <ellipse cx="34" cy="15" rx="12" ry="14"/>
    <ellipse cx="66" cy="15" rx="12" ry="14"/>
    <ellipse cx="86" cy="38" rx="11" ry="13"/>
    <path d="M50 40 C66 40 80 56 80 70 C80 82 68 86 58 82 C54 80 46 80 42 82 C32 86 20 82 20 70 C20 56 34 40 50 40 Z"/>
  </symbol>
</svg>
<main class="stage">

  <section class="card card--front" aria-label="Business card front">
    <svg class="card__shapes" viewBox="0 0 540 350" preserveAspectRatio="none" aria-hidden="true">
      <polygon points="0,92 392,62 440,82 300,350 0,350" fill="var(--paper)"/>
      <polygon points="540,0 540,350 300,350" fill="var(--olive-grey)"/>
    </svg>
    <svg class="paw paw--grey" role="img" aria-label="Paw print"><use href="#paw"/></svg>
    <svg class="paw paw--orange" role="img" aria-label="Paw print"><use href="#paw"/></svg>
    <p class="front__name">Hedgerowpups</p>
  </section>

  <section class="card card--back" aria-label="Business card back">
    <svg class="card__shapes" viewBox="0 0 540 350" preserveAspectRatio="none" aria-hidden="true">
      <polygon points="0,0 300,0 262,62 0,62" fill="var(--paper)"/>
      <polygon points="0,230 330,350 0,350" fill="var(--orange)"/>
    </svg>
    <p class="back__name">Hedgerowpups</p>
    <svg class="paw paw--orange" role="img" aria-label="Paw print"><use href="#paw"/></svg>
    <svg class="paw paw--grey" role="img" aria-label="Paw print"><use href="#paw"/></svg>
    <address class="back__contact">
      Lindelaan 27<br>
      B - 3270 Korbeek<br>
      Belgium
      <span class="gap"></span>
      +32471869203<br>
      mail@hedgerowpups.example<br>
      www.hedgerowpups.example
    </address>
  </section>

</main>
</body>
</html>
```